Hensby Estates Website and Logo Design

We need a new logo and website designed for 'Hensby Estates Ltd', which is a well established Guernsey property holding company founded in 1934.

The company does not currently have a website. The new website should be similar in style and layout to https://www.corvanhale.org/.

Target Market(s)

Industry, Media, Tenants

Industry/Entity Type

Property Management

Logo Text

HEL OR Hensby Estates Ltd OR HE

Coding

Coded - Design and coding required

Number of Pages Required

4 page

Font styles to use
Other font styles liked:
• Helvetica

Requirements
Must have
• The logo laying over the picture (like https://www.corvanhale.org/).
• Big pictures on homepage (like https://www.corvanhale.org/)

```html
<!DOCTYPE html>
<html lang="en">
<head>
<meta charset="utf-8">
<title>Hensby Estates Ltd — Guernsey Property Holding Company</title>
<link rel="stylesheet" href="https://fonts.googleapis.com/css2?family=Cinzel:wght@400;500&family=Open+Sans:wght@300;400;600&display=swap">
<style>
  :root {
    --sky-top: #3a3a66;
    --sky-mid: #4a4568;
    --town: #3d3f55;
    --water: #1f2a3e;
    --ink: #0f1116;
    --text: #f3eff3;
    --title: #e6dfe5;
    --soft: #d8d3dc;
    --accent: #c9953a;
    --rule: rgba(220, 215, 230, 0.45);
  }
  * { margin: 0; padding: 0; box-sizing: border-box; }
  html, body { width: 1200px; height: 762px; overflow: hidden; background: var(--ink); }
  .hero {
    position: relative;
    width: 1200px;
    height: 762px;
    overflow: hidden;
    font-family: "Open Sans", Helvetica, Arial, sans-serif;
    color: var(--text);
  }
  .hero-photo {
    position: absolute;
    inset: 0;
    background:
      linear-gradient(180deg, var(--sky-top) 0%, var(--sky-mid) 32%, #4b4a62 42%, var(--town) 58%, #2e3344 74%, var(--water) 86%, #1a2335 100%);
  }
  .brand {
    position: absolute;
    left: 40px;
    top: 24px;
    display: flex;
    align-items: center;
    gap: 10px;
    color: var(--text);
    text-decoration: none;
    font-family: "Open Sans", Helvetica, Arial, sans-serif;
    font-weight: 400;
    font-size: 15px;
    letter-spacing: 1px;
  }
  .brand-square {
    width: 14px;
    height: 14px;
    background: var(--text);
  }
  .main-nav {
    position: absolute;
    top: 0;
    right: 45px;
    display: flex;
    align-items: center;
    height: 68px;
  }
  .main-nav a {
    color: var(--text);
    text-decoration: none;
    font-size: 12px;
    letter-spacing: 1.6px;
    text-transform: uppercase;
    margin-left: 82px;
  }
  .main-nav a.is-current { color: var(--accent); }
  .main-nav a.nav-contact {
    background: var(--ink);
    height: 68px;
    width: 123px;
    display: flex;
    align-items: center;
    justify-content: center;
    margin-left: 62px;
  }
  .frame { position: absolute; inset: 0; pointer-events: none; }
  .headline {
    position: absolute;
    left: 0;
    width: 1224px;
    text-align: center;
  }
  .tagline { top: 296px; font-size: 22px; font-weight: 300; color: var(--soft); letter-spacing: 0.5px; }
  .place {
    top: 306px;
    font-size: 110px;
    font-weight: 600;
    color: var(--title);
    letter-spacing: -2px;
    line-height: 1.15;
  }
  .kind {
    top: 448px;
    font-family: "Cinzel", Georgia, serif;
    font-weight: 500;
    font-size: 25px;
    letter-spacing: 2.5px;
    color: var(--text);
    width: 1214px;
  }
  .founded { top: 515px; font-size: 12px; letter-spacing: 2px; color: var(--soft); width: 1202px; }
  .scroll-down {
    position: absolute;
    left: 547px;
    top: 639px;
    width: 120px;
    height: 123px;
    background: var(--ink);
    display: flex;
    align-items: center;
    justify-content: center;
  }
</style>
</head>
<body>
<main class="hero">
  <div class="hero-photo" role="img" aria-label="Photograph of a harbour town on Guernsey with sailing boats moored in front of a hillside of houses under a dusky sky"></div>

  <header>
    <a class="brand" href="#">
      <span class="brand-square" aria-hidden="true"></span>
      <span class="brand-name">Hensby Estates Ltd</span>
    </a>
    <nav class="main-nav">
      <a href="#">Why Guernsey?</a>
      <a href="#">Yesterday</a>
      <a href="#" class="is-current">Today</a>
      <a href="#">Tomorrow</a>
      <a href="#" class="nav-contact">Contact Us</a>
    </nav>
  </header>

  <svg class="frame" width="1200" height="762" aria-hidden="true">
    <line x1="312" y1="271" x2="879" y2="271" stroke="var(--rule)" stroke-width="1"/>
    <line x1="312" y1="271" x2="312" y2="330" stroke="var(--rule)" stroke-width="1"/>
    <line x1="902" y1="346" x2="902" y2="497" stroke="var(--rule)" stroke-width="1"/>
    <line x1="700" y1="497" x2="902" y2="497" stroke="var(--rule)" stroke-width="1"/>
  </svg>

  <p class="headline tagline">A family owned</p>
  <h1 class="headline place">Guernsey</h1>
  <p class="headline kind">PROPERTY HOLDING COMPANY</p>
  <p class="headline founded">FOUNDED IN 1934</p>

  <a class="scroll-down" href="#" aria-label="Scroll down">
    <svg width="70" height="70" viewBox="0 0 70 70" aria-hidden="true">
      <circle cx="35" cy="35" r="33" fill="none" stroke="#ffffff" stroke-width="2"/>
      <polyline points="20,29 35,44 50,29" fill="none" stroke="#ffffff" stroke-width="2"/>
    </svg>
  </a>
</main>
</body>
</html>
```